Flyer for longday centre (Childcare Centre)

We need a marketing flyer for our long day (Childcare) centre targeting childcare enrolments for 2016.

The name of the childcare is: Wexbury Vale Early Childhood Learning Centre
Location: will be provided later
Telephone: will be provided later
Email: will be provided later

The message of the flyer should have limited places now available for 2016. Enrol now.

Target Market(s)

Parents and Families

Industry/Entity Type

Childcare

Font styles to use
Sans Serif

Requirements
Must have
• Come and see why more and more families are switching to Wexbury Vale.
• We invite parents to come along to explore our facilities and our children's programs.
• We also run a government approved and funded Kindergarten program.
Nice to have
• Opening hours: 6am to 6:30pm Monday to Friday

```html
<!DOCTYPE html>
<html lang="en">
<head>
<meta charset="utf-8">
<title>Wexbury Vale Early Childhood Learning Centre – Enrol Now</title>
<link rel="stylesheet" href="https://fonts.googleapis.com/css2?family=Arimo:ital,wght@0,400;0,700;1,700&display=swap">
<style>
  :root {
    --green: #1fa24a;
    --red: #d0213a;
    --crimson: #c4163a;
    --yellow: #ffe98a;
    --cream: #fffbe6;
    --grey: #555a5e;
    --white: #ffffff;
  }
  * { margin: 0; padding: 0; box-sizing: border-box; }
  html, body { width: 849px; height: 1200px; overflow: hidden; }
  body { font-family: "Arimo", Arial, sans-serif; background: var(--white); }
  .flyer {
    position: relative; width: 849px; height: 1200px; overflow: hidden;
    background: linear-gradient(180deg, #ffffff 0%, #fffdf2 55%, var(--cream) 85%);
  }
  .hero-photo {
    position: absolute; left: 0; top: 0; width: 849px; height: 380px;
    background: linear-gradient(120deg, #e9e4dc 0%, #f4f1ec 45%, #dcd6cc 100%);
  }
  .arch { position: absolute; left: 0; top: 0; width: 849px; height: 545px; }
  .mascot-art {
    position: absolute; left: 319px; top: 318px; width: 210px; height: 180px;
    border-radius: 30px;
    background: radial-gradient(ellipse at 50% 50%, #f6c94a 0%, #f4a23a 40%, rgba(244,162,58,0) 70%);
  }
  .centre-name {
    position: absolute; left: 0; top: 548px; width: 100%; text-align: center;
    color: var(--green); font-weight: 700; font-size: 80px; letter-spacing: 1px; line-height: 1;
  }
  .centre-type {
    position: absolute; left: 0; top: 636px; width: 100%; text-align: center;
    color: var(--green); font-size: 32px; letter-spacing: 1px; line-height: 1;
  }
  .info-box {
    position: absolute; top: 708px; width: 310px; height: 144px; border-radius: 14px;
    color: var(--white); font-size: 25px; line-height: 1.25; text-align: center;
    display: flex; align-items: center; justify-content: center; padding: 10px 20px;
    box-shadow: 0 4px 8px rgba(0,0,0,0.2);
  }
  .info-box.visit { left: 90px; background: linear-gradient(180deg, #e2455c, var(--red)); }
  .info-box.kinder { left: 450px; background: linear-gradient(180deg, #35b85d, var(--green)); }
  .offer {
    position: absolute; left: 0; top: 876px; width: 100%; text-align: center;
    color: var(--green); font-weight: 700; font-size: 56px; line-height: 1.08;
  }
  .offer .enrol { color: var(--red); }
  .hours {
    position: absolute; left: 0; top: 1000px; width: 100%; text-align: center;
    color: var(--grey); font-weight: 700; font-size: 32px;
  }
  .contact-band {
    position: absolute; left: 0; top: 1050px; width: 849px; height: 150px;
    background: var(--crimson);
  }
  .call-pill {
    position: absolute; left: 198px; top: 1070px; width: 453px; height: 62px;
    border-radius: 31px; background: var(--green); color: var(--white);
    font-weight: 700; font-size: 40px; text-align: center; line-height: 62px;
  }
  .address {
    position: absolute; left: 0; top: 1148px; width: 100%; text-align: center;
    color: var(--white); font-size: 24px;
  }
</style>
</head>
<body>
  <main class="flyer">
    <div class="hero-photo" role="img" aria-label="Photo of a mother and a smiling toddler lying on a soft white carpet"></div>

    <svg class="arch" viewBox="0 0 849 545">
      <defs>
        <linearGradient id="archFill" x1="0" y1="0" x2="0" y2="1">
          <stop offset="0" stop-color="#ffffff"/>
          <stop offset="0.6" stop-color="#ffffff"/>
          <stop offset="1" stop-color="#ffe98a"/>
        </linearGradient>
        <path id="slogan-path" d="M 180 520 A 244 244 0 0 1 668 520"/>
      </defs>
      <path d="M 150 545 L 150 520 A 274 274 0 0 1 698 520 L 698 545 Z" fill="#c4163a"/>
      <path d="M 188 545 L 188 520 A 236 236 0 0 1 660 520 L 660 545 Z" fill="#f7c21b"/>
      <path d="M 194 545 L 194 520 A 230 230 0 0 1 654 520 L 654 545 Z" fill="url(#archFill)"/>
      <text font-family="Arimo, Arial, sans-serif" font-style="italic" font-weight="700" font-size="27" fill="#ffffff">
        <textPath href="#slogan-path" startOffset="50%" text-anchor="middle">Come &amp; see why more &amp; more families are switching to</textPath>
      </text>
    </svg>

    <div class="mascot-art" role="img" aria-label="Cartoon illustration of children with numbers and letters"></div>

    <h1 class="centre-name">WEXBURY VALE</h1>
    <p class="centre-type">EARLY CHILDHOOD LEARNING CENTRE</p>

    <p class="info-box visit">Come and explore our facilities and programs we have for the children.</p>
    <p class="info-box kinder">We run a government approved and funded kindergarten program.</p>

    <p class="offer">LIMITED PLACES AVAILABLE<br>FOR 2016 <span class="enrol">ENROL NOW</span></p>
    <p class="hours">Open Monday to Friday 6am to 6.30pm</p>

    <div class="contact-band"></div>
    <p class="call-pill">Call: 01234 567890</p>
    <p class="address">Address Here, Address Here, Address Here, Address Here</p>
  </main>
</body>
</html>
```